Center for Cellular Datawork wordpress design

We need a wordpress design for the new Center for Cellular Datawork at the Marrowfield University. We are a research institute focused on medical and biological research involving big data and informatics. The website has to be eyecatching and appropriate for an academic context, with easily updated content.

Press release here: http://www.mfhs.marrowfield-u.edu/news/News_Releases/2013/02/cellular/

We would prefer to use images from our research labs over stock art, but feel free to use placeholders for now. Please contact me if there are specific types of images you need.

Target Market(s)

Tech-savvy academics, faculty, students, general laypeople

Industry/Entity Type

Medical

Requirements
Must have
• Use existing logo (attached, other versions available upon request)

Sections for:
Mission statement (draft version attached)
Educational Programs: there is only one at the moment, but we will need the option to add more
Faculty members/resident staff (contact database); webform to apply to join
Events calendar/list
Emphasis on search engine optimization
Nice to have
• News/publication tabs for the front page (similar to those on http://www.ovrek.marrowfield-u.edu/)

It would be helpful if you could use the Marrowfield color palette: http://www.marrowfield-u.edu/webservices/styleguide/color.html

```html
<!DOCTYPE html>
<html lang="en">
<head>
<meta charset="utf-8">
<title>Center for Cellular Datawork</title>
<link rel="stylesheet" href="https://fonts.googleapis.com/css2?family=Arimo:wght@400;700&display=swap">
<style>
:root{
  --navy:#0a2a82;
  --logo-blue:#2b3686;
  --red:#a0102b;
  --header-bg:#f2f2f2;
  --panel:#f0f0f0;
  --beige:#c6c1b4;
  --btn:#2a2a2a;
  --text:#2b2b2b;
  --muted:#6a665d;
  --white:#ffffff;
}
*{margin:0;padding:0;box-sizing:border-box}
html,body{width:942px;height:1200px;overflow:hidden}
body{background:var(--navy);font-family:"Arimo",Arial,sans-serif;color:var(--text);position:relative}
.abs{position:absolute}
.header{left:78px;top:0;width:786px;height:113px;background:var(--header-bg)}
.logo{left:16px;top:24px;display:flex;align-items:flex-start;gap:12px}
.logo-mark{width:48px;height:48px;background:var(--logo-blue);margin-top:4px}
.logo-name{color:var(--logo-blue);font-size:27px;line-height:28px;font-weight:400}
.util{top:10px;font-size:10px;color:#444;text-align:center}
.util svg{display:block;margin:6px auto 0}
.search{left:572px;top:57px;width:196px;height:25px;background:#fff;border:1px solid #d6d6d6;font-size:9px;font-style:italic;color:#888;padding:7px 9px}
.search svg{position:absolute;right:8px;top:6px}
.nav{left:78px;top:113px;width:786px;height:48px;background:var(--navy)}
.nav a{position:absolute;top:0;height:47px;line-height:47px;color:#fff;font-size:11px;text-decoration:none;letter-spacing:.2px}
.nav a.active{background:var(--red);padding:0 13px}
.shade{left:78px;top:161px;width:786px;height:15px;background:linear-gradient(#cfd3dd,#f4f4f4)}
.slider{left:78px;top:176px;width:548px;height:262px;background:linear-gradient(110deg,#dfe6ec,#b9c6cf 45%,#6f8694)}
.arrow{width:36px;height:36px;border-radius:50%;background:rgba(120,120,120,.55)}
.side-photo{left:635px;top:176px;width:229px;height:153px;background:linear-gradient(120deg,#c9ced3,#8f9aa3)}
.promo{left:635px;top:329px;width:229px;height:109px;background:var(--red);color:#fff;padding:10px 10px}
.promo .kicker{font-size:13px}
.promo .title{font-size:21px;line-height:22px}
.promo p{font-size:9px;line-height:14px;margin-top:5px}
.btn{position:absolute;background:var(--btn);color:#fff;font-size:9.5px;text-align:center;border-radius:3px;line-height:22px;height:22px;width:71px}
.pillars{left:78px;top:438px;width:786px;height:127px;background:#f4f4f4}
.pillar{position:absolute;top:0}
.pillar h2{font-size:20px;font-weight:400;color:var(--red);margin-top:16px;letter-spacing:-.2px}
.pillar p{font-size:9.2px;line-height:14.2px;margin-top:9px;width:226px}
.divider{top:16px;width:1px;height:94px;background:#dcdcdc}
.main{left:78px;top:571px;width:557px;height:533px;background:#fff}
.main h1{position:absolute;left:13px;top:16px;font-size:20px;font-weight:400;color:var(--red)}
.main .intro{position:absolute;left:15px;top:49px;width:535px;font-size:9.2px;line-height:14.2px}
.tab{font-size:20px;color:var(--red);top:170px}
.tab.on{left:7px;top:165px;width:85px;height:34px;background:var(--panel);padding:9px 0 0 14px}
.news{left:7px;top:199px;width:536px;height:334px;background:var(--panel)}
.news .photo{position:absolute;left:10px;top:16px;width:511px;height:234px;background:linear-gradient(135deg,#dfeaf3,#8fb4d4 55%,#4f80ad)}
.news p{position:absolute;left:12px;top:268px;width:512px;font-size:9.2px;line-height:14.2px}
.events{left:635px;top:571px;width:229px;height:262px;background:var(--beige)}
.gap{left:635px;top:833px;width:229px;height:8px;background:#e8e6e0}
.panel-title{position:absolute;font-size:20px;color:var(--red);font-weight:400}
.event{position:absolute;left:12px;width:210px;height:58px}
.event .thumb{position:absolute;left:0;top:0;width:58px;height:58px;background:linear-gradient(#e9edf0,#9fb2c1);border:2px solid #eee}
.event .txt{position:absolute;left:67px;top:0;width:140px;font-size:9.6px;line-height:14px;color:var(--muted)}
.event .date{color:#1b2f78;display:block}
.faculty{left:635px;top:841px;width:229px;height:263px;background:var(--beige)}
.face{position:absolute;width:46px;height:46px;border:2px solid #eee}
.fbtn{position:absolute;top:214px;height:23px;background:var(--btn);color:#fff;font-size:13px;line-height:23px;text-align:center;border-radius:3px}
.footer-links{left:86px;top:1120px;font-size:9.8px;color:#dfe4f3;word-spacing:1px}
.footer-links span{margin:0 7px;color:#bfc6e0}
.copy{left:86px;top:1148px;font-size:9.6px;color:#dfe4f3}
.social{top:1146px;width:18px;height:18px;border-radius:3px;background:#5b80c8}
</style>
</head>
<body>

<header class="abs header">
  <div class="abs logo">
    <div class="logo-mark"></div>
    <div class="logo-name">Center for<br>Cellular Datawork</div>
  </div>
  <div class="abs util" style="left:680px">HOME
    <svg width="14" height="18" viewBox="0 0 14 18"><path d="M7 1a6 6 0 0 0-6 6c0 4 6 10 6 10s6-6 6-10a6 6 0 0 0-6-6z" fill="none" stroke="#aaa" stroke-width="1.6"/><circle cx="7" cy="7" r="2" fill="#aaa"/></svg>
  </div>
  <div class="abs util" style="left:726px">ABOUT
    <svg width="16" height="18" viewBox="0 0 16 18"><circle cx="8" cy="5" r="4" fill="#aaa"/><path d="M0 18c0-5 3-8 8-8s8 3 8 8z" fill="#aaa"/></svg>
  </div>
  <div class="abs search">Search here..
    <svg width="13" height="13" viewBox="0 0 13 13"><circle cx="5.5" cy="5.5" r="4" fill="none" stroke="#888" stroke-width="2"/><path d="M8.5 8.5l3.5 3.5" stroke="#888" stroke-width="2.2"/></svg>
  </div>
</header>

<nav class="abs nav">
  <a class="active" style="left:52px">COURSES AND PROGRAMS</a>
  <a style="left:236px">LATEST NEWS</a>
  <a style="left:340px">LATEST EVENTS</a>
  <a style="left:455px">MEMBERS</a>
  <a style="left:537px">LINKS</a>
  <a style="left:596px">CONTACT US</a>
  <a style="left:694px">HELP</a>
</nav>
<div class="abs shade"></div>

<div class="abs slider" role="img" aria-label="Two researchers in lab coats examining a flask in a laboratory">
  <div class="abs arrow" style="left:14px;top:120px"><svg width="36" height="36"><path d="M21 12l-7 6 7 6z" fill="#fff"/></svg></div>
  <div class="abs arrow" style="left:496px;top:120px"><svg width="36" height="36"><path d="M15 12l7 6-7 6z" fill="#fff"/></svg></div>
</div>
<div class="abs side-photo" role="img" aria-label="Scientist in protective glasses handling red sample bottles"></div>
<div class="abs promo">
  <div class="kicker">EDUCATIONAL</div>
  <div class="title">PROGRAMS</div>
  <p>The primary role of CCD is to provide an academic home for basic science.</p>
  <div class="btn" style="left:143px;top:73px">Learn More</div>
</div>

<section class="abs pillars">
  <div class="pillar" style="left:16px">
    <h2>CATALYZING RESEARCH</h2>
    <p>The primary role of CCD is to provide an academic home for basic science faculty in cellular datawork, as well as mechanisms to connect genetic ..</p>
  </div>
  <div class="btn" style="left:173px;top:100px">Learn More</div>
  <div class="abs divider" style="left:262px"></div>
  <div class="pillar" style="left:277px">
    <h2>FACILITATING EDUCATION</h2>
    <p>Simply put, there aren’t enough trainees or facultythere is a shortage of scientists to conduct this interdisciplinary research and fully realize personalized medicine.</p>
  </div>
  <div class="btn" style="left:448px;top:100px">Learn More</div>
  <div class="abs divider" style="left:531px"></div>
  <div class="pillar" style="left:547px">
    <h2>CAMPUS LEADERSHIP</h2>
    <p>Within the School of Medicine, CCD will play a leadership role in advising Departments, Centers, and Institutes in hiring,</p>
  </div>
  <div class="btn" style="left:700px;top:100px">Learn More</div>
</section>

<main class="abs main">
  <h1>WELCOME TO CELLULAR DATAWORK</h1>
  <p class="intro">Sed ut perspiciatis unde omnis iste natus error sit voluptatem accusantium doloremque laudantium, totam rem aperiam, eaque ipsa quae ab illo inventore veritatis et quasi architecto beatae vitae dicta sunt explicabo. Nemo enim ipsam voluptatem quia voluptas sit aspernatur aut odit aut fugit, sed quia consequuntur magni dolores eos qui ratione voluptatem sequi nesciunt. Neque porro quisquam est, qui dolorem ipsum quia dolor sit amet, consectetur, adipisci velit, sed quia non numquam eius modi tempora incidunt ut labore et dolore magnam aliquam quaerat voluptatem. Ut enim ad minima veniam, quis nostrum</p>
  <div class="btn" style="left:13px;top:125px">Learn More</div>
  <div class="abs tab on">NEWS</div>
  <div class="abs tab" style="left:105px;top:174px">PUPLICATIONS</div>
  <div class="abs news">
    <div class="photo" role="img" aria-label="Blue DNA double helix illustration"></div>
    <p>Sed ut perspiciatis unde omnis iste natus error sit voluptatem accusantium doloremque laudantium, totam rem aperiam, eaque ipsa quae ab illo inventore veritatis et quasi architecto beatae vitae dicta sunt explicabo. Nemo enim ipsam voluptatem quia voluptas sit aspernatur aut odit aut fugit, sed quia consequuntur magni dolores eos</p>
    <div class="btn" style="left:446px;top:300px">Learn More</div>
  </div>
</main>

<aside class="abs events">
  <div class="panel-title" style="left:12px;top:19px">EVENTS</div>
  <svg class="abs" style="left:202px;top:8px" width="20" height="20"><circle cx="10" cy="10" r="10" fill="#1c1c1c"/><path d="M8 6l5 4-5 4z" fill="#fff"/></svg>
  <div class="event" style="top:39px"><div class="thumb" role="img" aria-label="Doctor portrait"></div><div class="txt">Sed commodo, sem a pellen mollis enim, ac pulvinar odio elit in tincidunt.<span class="date">Mar-03-2013</span></div></div>
  <div class="event" style="top:110px"><div class="thumb" role="img" aria-label="Medical team group photo"></div><div class="txt">Sed commodo, sem a pellen mollis enim, ac pulvinar odio elit in tincidunt.<span class="date">Mar-03-2013</span></div></div>
  <div class="event" style="top:182px"><div class="thumb" role="img" aria-label="Researchers at a microscope"></div><div class="txt">Sed commodo, sem a pellen mollis enim, ac pulvinar odio elit in tincidunt.<span class="date">Mar-03-2013</span></div></div>
</aside>
<div class="abs gap"></div>

<aside class="abs faculty">
  <div class="panel-title" style="left:9px;top:20px">FACULTY MEMBERS</div>
  <div class="face" role="img" aria-label="Faculty photo" style="left:10px;top:41px;background:#d6b9d6"></div>
  <div class="face" role="img" aria-label="Faculty photo" style="left:63px;top:41px;background:#b59b6a"></div>
  <div class="face" role="img" aria-label="Faculty photo" style="left:117px;top:41px;background:#5ab7c4"></div>
  <div class="face" role="img" aria-label="Faculty photo" style="left:171px;top:41px;background:#9cb067"></div>
  <div class="face" role="img" aria-label="Faculty photo" style="left:10px;top:98px;background:#c8a67f"></div>
  <div class="face" role="img" aria-label="Faculty photo" style="left:63px;top:98px;background:#c78c7e"></div>
  <div class="face" role="img" aria-label="Faculty photo" style="left:117px;top:98px;background:#d8b23a"></div>
  <div class="face" role="img" aria-label="Faculty photo" style="left:171px;top:98px;background:#4aa5a7"></div>
  <div class="face" role="img" aria-label="Faculty photo" style="left:10px;top:156px;background:#d6b9d6"></div>
  <div class="face" role="img" aria-label="Faculty photo" style="left:63px;top:156px;background:#b59b6a"></div>
  <div class="face" role="img" aria-label="Faculty photo" style="left:117px;top:156px;background:#5ab7c4"></div>
  <div class="face" role="img" aria-label="Faculty photo" style="left:171px;top:156px;background:#9cb067"></div>
  <div class="fbtn" style="left:11px;width:86px">Members</div>
  <div class="fbtn" style="left:102px;width:86px">Resident staff</div>
</aside>

<footer>
  <div class="abs footer-links">Home<span>|</span>About us<span>|</span>Courses and Programs<span>|</span>Latest News<span>|</span>Latest Events<span>|</span>Members<span>|</span>Links<span>|</span>Contact us<span>|</span>Help<span>|</span>Register<span>|</span>Member Login</div>
  <div class="abs copy">Copyright &nbsp;©&nbsp; 2013 &nbsp; www.cellulardatawork.org &nbsp; All rights reserved.</div>
  <div class="abs social" style="left:805px"></div>
  <div class="abs social" style="left:829px;background:#5cc0ea"></div>
</footer>

</body>
</html>
```